Lumo Brew Premium Matcha brand Label

This is a label design project for a luxury tea brand. Feel free to be creative within the guidelines.
Attached to this project is a document called “Private Label Design Requirements” with the design guidelines and template. There is another document called "Lumo Brew Packaging Instructions" this has more details necessary to stick to the guidelines in the first document.

I have also attached the certifications to be included as well as different variations of the logo for you to use.

If you have any questions, I am here.
Updates

Target Market(s)

Young, active, fun, enjoy the finer things

```html
<!DOCTYPE html>
<html lang="en">
<head>
<meta charset="UTF-8">
<title>Lumo Brew Premium Matcha Label</title>
<link href="https://fonts.googleapis.com/css2?family=Bebas+Neue&family=Lato:wght@400;700&display=swap" rel="stylesheet">
<style>
  :root {
    --bg: #ececec;
    --label-dark: #052a0c;
    --label-mid: #0f4a17;
    --pattern-a: #2f7d2a;
    --pattern-b: #8bc34a;
    --panel-light: #8cc152;
    --accent: #9ad14b;
    --text-light: #e8f3dc;
    --white: #ffffff;
    --dash: rgba(140, 193, 82, 0.45);
  }
  * { margin: 0; padding: 0; box-sizing: border-box; }
  html, body { width: 1200px; height: 1000px; overflow: hidden; background: var(--bg); }
  .canvas { position: relative; width: 1200px; height: 1000px; }
  .label {
    position: absolute; left: 43px; top: 395px; width: 1114px; height: 210px;
    background: var(--label-dark); overflow: hidden;
    font-family: "Lato", sans-serif; color: var(--text-light);
  }
  .dash-line { position: absolute; left: 0; right: 0; border-top: 2px dashed var(--dash); }
  .dash-line.top { top: 18px; }
  .dash-line.bottom { bottom: 18px; }
  .back-panel {
    position: absolute; left: 0; top: 0; width: 412px; height: 210px;
    background: linear-gradient(90deg, var(--label-dark), #0a3812 50%, var(--label-dark));
  }
  .back-frame {
    position: absolute; left: 62px; top: 36px; width: 300px; height: 140px;
    border: 2px dashed var(--dash);
  }
  .back-text {
    position: absolute; left: 80px; top: 128px; font-size: 9px; line-height: 1.45;
  }
  .front-band {
    position: absolute; left: 412px; top: 0; width: 280px; height: 210px;
    background: linear-gradient(135deg, var(--pattern-a), var(--label-mid) 50%, var(--pattern-a));
  }
  .front-panel {
    position: absolute; left: 81px; top: 42px; width: 118px; height: 126px;
    background: var(--panel-light); text-align: center;
    display: flex; flex-direction: column; align-items: center; padding-top: 10px;
  }
  .brand-mark {
    width: 46px; height: 46px; border-radius: 50%; background: var(--white);
    display: flex; align-items: center; justify-content: center;
    font-family: "Lato", sans-serif; font-weight: 700; font-size: 8px; color: var(--label-dark);
  }
  .product-name {
    margin-top: 10px; font-family: "Bebas Neue", sans-serif; font-size: 15px;
    line-height: 0.95; color: var(--white); letter-spacing: 0.3px;
  }
  .net-weight {
    margin-top: 12px; font-family: "Bebas Neue", sans-serif; font-size: 11px; color: var(--white);
  }
  .info-panel { position: absolute; left: 758px; top: 36px; width: 340px; }
  .info-title {
    font-family: "Bebas Neue", sans-serif; font-size: 13px; color: var(--accent); letter-spacing: 0.4px;
  }
  .instructions-head { margin-top: 6px; font-size: 10px; font-weight: 700; text-decoration: underline; }
  .instructions { list-style: none; font-size: 9px; line-height: 1.4; margin-top: 1px; }
  .instructions li::before { content: "• "; }
  .cert-row { display: flex; align-items: center; gap: 10px; margin-top: 6px; }
  .cert-badge { width: 40px; height: 30px; background: #3b6fb6; border-radius: 3px; }
  .cert-badge.round { width: 32px; height: 32px; border-radius: 50%; background: #2e7d32; border: 2px solid var(--white); }
  .storage-note {
    font-family: "Bebas Neue", sans-serif; font-size: 13px; line-height: 1; color: var(--accent); margin-left: 6px;
  }
</style>
</head>
<body>
<div class="canvas">
  <div class="label">
    <div class="back-panel" role="img" aria-label="Faint geometric green pattern on the back panel">
      <div class="back-frame"></div>
      <p class="back-text">Product of Japan<br>Distributed by Lumo Brew Co, Riverton, Ga<br>Certified Organic by Terra</p>
    </div>
    <div class="front-band" role="img" aria-label="Interlocking green geometric pattern band">
      <div class="front-panel">
        <div class="brand-mark">Lumo Brew</div>
        <p class="product-name">Premium Organic<br>Ceremonial Matcha</p>
        <p class="net-weight">Net Wt: 30g</p>
      </div>
    </div>
    <div class="dash-line top"></div>
    <div class="dash-line bottom"></div>
    <div class="info-panel">
      <p class="info-title">Premium Organic Japanese Matcha Green Tea</p>
      <p class="instructions-head">Instructions</p>
      <ul class="instructions">
        <li>2 tsp of Matcha</li>
        <li>2oz of Water (160-170 degrees F)</li>
        <li>Whisk in W formation until frothy</li>
        <li>Sweeten to taste</li>
      </ul>
      <div class="cert-row">
        <div class="cert-badge" role="img" aria-label="Certification badge"></div>
        <div class="cert-badge round" role="img" aria-label="Organic certification badge"></div>
        <p class="storage-note">Keep Refrigerated<br>For Quality</p>
      </div>
    </div>
  </div>
</div>
</body>
</html>
```